Business Cards for Corvantis LLC

We need business cards for a new company called “Corvantis LLC”. This is a technology process improvement company providing a comprehensive assessment of the technology used to run their business. The documentation and review process delivers the visibility and reassurance they need to protect their business and plan for the future. The product is called “Halvorne Ledgerwork”. Our primary target is small-medium size businesses, with the deliverables going to the decision maker. We would like to see the designs use the color blue. Our tag line is CLEAR SYSTEMS · CONFIDENT DECISIONS.

Industry/Entity Type

Business

Contact Information for Business Card

Tag line should be on back of card - it does not have to be upper case.

Requirements
Must have
• Please use information when laying out card:
• Name: Darnell Pruitt
• Title: Partner
• Phone Number: (877)555-0143
• Email: dell@corvantisllc.com
• Website: http://corvantisllc.com

```html
<!DOCTYPE html>
<html lang="en">
<head>
<meta charset="utf-8">
<title>Corvantis LLC — Business Card</title>
<link href="https://fonts.googleapis.com/css2?family=Open+Sans:wght@400;600;700&display=swap" rel="stylesheet">
<style>
  :root{
    --backdrop:#17181a;
    --card:#2a2b2e;
    --card-deep:#1d1d1f;
    --blue:#1f72c2;
    --blue-light:#2c86d6;
    --blue-text:#2a7fd0;
    --tag-text:#8fc1ef;
    --white:#f4f5f7;
    --muted:#b9c0c8;
  }
  *{box-sizing:border-box;margin:0;padding:0}
  html,body{width:1200px;height:1200px;overflow:hidden;background:var(--backdrop)}
  body{font-family:"Open Sans",Arial,sans-serif;position:relative}
  .card{position:absolute;left:180px;width:840px;height:480px;border-radius:28px;background:var(--card);overflow:hidden;box-shadow:0 14px 40px rgba(0,0,0,.55)}
  .card--front{top:75px}
  .card--back{top:645px}

  .brand{position:absolute;display:flex;align-items:center;gap:12px;color:var(--blue-text);font-weight:700;letter-spacing:.5px;white-space:nowrap}
  .brand__mark{background:var(--blue-text);border-radius:3px}
  .card--front .brand{left:60px;top:58px;font-size:32px}
  .card--front .brand__mark{width:26px;height:26px}

  .person{position:absolute;right:88px;top:140px;text-align:right;color:var(--white);white-space:nowrap}
  .person__name{font-size:40px;font-weight:600;letter-spacing:1px;line-height:1.1}
  .person__title{font-size:24px;font-weight:400;letter-spacing:1px;margin-top:4px}
  .person__rule{position:absolute;right:56px;top:144px;width:7px;height:92px;background:var(--blue);border-radius:3px}

  .contact{position:absolute;display:flex;align-items:center;gap:12px;color:var(--muted);font-size:18px;white-space:nowrap}
  .contact-band{position:absolute;left:40px;top:360px;height:84px;width:700px;display:flex}
  .contact-band__web{width:290px;background:var(--blue)}
  .contact-band__mail{flex:1;background:var(--blue-light)}
  .phone-box{position:absolute;left:250px;top:246px;width:300px;height:114px;background:var(--card-deep);display:flex;flex-direction:column;align-items:center;justify-content:center;gap:10px;color:var(--muted);font-size:19px}
  .contact--web{left:70px;top:388px;color:#d6e6f6}
  .contact--mail{left:400px;top:388px;color:#e6f0fa}
  .icon{flex:none}

  .band{position:absolute;left:0;width:100%;height:96px;background:var(--blue)}
  .band--top{top:0}
  .band--bottom{bottom:0}
  .card--back .brand{left:0;right:0;top:180px;justify-content:center;font-size:48px}
  .card--back .brand__mark{width:38px;height:38px}
  .tagline{position:absolute;left:0;right:0;top:262px;text-align:center;color:var(--tag-text);font-size:21px;letter-spacing:.5px}
</style>
</head>
<body>

<section class="card card--front" aria-label="Card front">
  <div class="brand"><span class="brand__mark"></span>Corvantis LLC</div>

  <div class="person__rule"></div>
  <div class="person">
    <div class="person__name">DARNELL PRUITT</div>
    <div class="person__title">PARTNER</div>
  </div>

  <div class="contact-band">
    <div class="contact-band__web"></div>
    <div class="contact-band__mail"></div>
  </div>

  <div class="phone-box">
    <svg class="icon" width="26" height="26" viewBox="0 0 24 24" aria-hidden="true">
      <rect width="24" height="24" rx="3" fill="#2a7fd0"/>
      <path d="M8 5.5l2 3-1.3 1.2c.8 1.8 2 3 3.6 3.8L13.5 12l3 2-1 2.5c-4.5-.4-8.3-4.2-8.7-8.8z" fill="#fff"/>
    </svg>
    <span>(877)555-0143</span>
  </div>

  <div class="contact contact--web">
    <svg class="icon" width="24" height="24" viewBox="0 0 24 24" aria-hidden="true">
      <circle cx="12" cy="12" r="10" fill="#1b1c1e"/>
      <circle cx="12" cy="12" r="7" fill="none" stroke="#b9c0c8" stroke-width="1.3"/>
      <ellipse cx="12" cy="12" rx="3" ry="7" fill="none" stroke="#b9c0c8" stroke-width="1.3"/>
      <path d="M5 12h14" stroke="#b9c0c8" stroke-width="1.3"/>
    </svg>
    <span>http://corvantisllc.com</span>
  </div>

  <div class="contact contact--mail">
    <svg class="icon" width="28" height="24" viewBox="0 0 28 24" aria-hidden="true">
      <rect width="28" height="24" fill="#111"/>
      <rect x="4" y="6" width="20" height="13" fill="none" stroke="#2c86d6" stroke-width="1.6"/>
      <path d="M4 6l10 7 10-7" fill="none" stroke="#2c86d6" stroke-width="1.6"/>
    </svg>
    <span>dell@corvantisllc.com</span>
  </div>
</section>

<section class="card card--back" aria-label="Card back">
  <div class="band band--top"></div>
  <div class="brand"><span class="brand__mark"></span>Corvantis LLC</div>
  <p class="tagline">clear systems · confident decisions.</p>
  <div class="band band--bottom"></div>
</section>

</body>
</html>
```